mediation practice website build

Looking to create a website for new civil mediation practice. Pages would be "home", "about us", "about mediation", "scheduling" (perhaps with some kind of calendar function), "contact us". Would love to be able to update content/text myself.
Target Market(s)
Small to midsize businesses and attorneys representing those size businesses in pending disputes.
Industry/Entity Type
Build
Look and feel
Each slider illustrates characteristics of the customer's brand and the style your logo design should communicate.

```html
<!DOCTYPE html>
<html lang="en">
<head>
<meta charset="utf-8">
<title>Linden Mediation</title>
<link href="https://fonts.googleapis.com/css2?family=Arimo:wght@400;700&display=swap" rel="stylesheet">
<style>
  :root {
    --backdrop: #7d7e79;
    --rule-dark: #3a3a38;
    --navy: #0e4a84;
    --navy-deep: #00203f;
    --ink: #333333;
    --link: #2a7fc4;
    --white: #ffffff;
    --photo-a: #eef0f3;
    --photo-b: #3a3f4a;
  }
  * { margin: 0; padding: 0; box-sizing: border-box; }
  html, body {
    width: 1200px; height: 720px; overflow: hidden;
    background: var(--backdrop);
    font-family: "Arimo", Arial, sans-serif;
  }
  .page {
    position: relative;
    width: 1345px; height: 807px;
    transform: scale(0.89219);
    transform-origin: 0 0;
  }
  .top-rule {
    position: absolute; left: 0; top: 22px; width: 1345px; height: 6px;
    background: var(--rule-dark);
  }
  .header {
    position: absolute; left: 0; top: 28px; width: 1345px; height: 61px;
    background: var(--white);
    border-bottom: 1px dashed #8a8a8a;
  }
  .main-nav {
    position: absolute; left: 202px; top: 26px;
    display: flex; gap: 41px;
    list-style: none;
  }
  .main-nav li {
    font-size: 14px; font-weight: 700; letter-spacing: 1.2px;
    color: var(--navy);
  }
  .brand {
    position: absolute; left: 940px; top: 24px;
    display: flex; align-items: center; gap: 8px;
    font-size: 19px; font-weight: 700; line-height: 22px;
    color: var(--navy);
  }
  .brand-mark {
    width: 14px; height: 14px; border-radius: 50%; background: var(--navy);
  }
  .content {
    position: absolute; left: 192px; top: 89px; width: 960px; height: 638px;
    background: var(--white);
  }
  .hero {
    position: absolute; left: 56px; top: 12px; width: 864px; height: 274px;
    background: linear-gradient(180deg, var(--photo-a) 0%, #b9bec7 30%, var(--photo-b) 100%);
  }
  .section-title {
    position: absolute;
    font-size: 18px; font-weight: 700; color: var(--navy);
    border-bottom: 2px solid var(--navy);
    padding-bottom: 7px;
  }
  .copy {
    position: absolute; width: 600px;
    font-size: 12px; font-weight: 700; line-height: 14px;
    color: var(--ink); text-align: justify; letter-spacing: 0.75px;
  }
  .read-more {
    position: absolute; width: 600px; text-align: right;
    font-size: 12.5px; font-weight: 700; color: var(--link); letter-spacing: 0.6px;
  }
  .calendar-month {
    position: absolute; left: 651px; top: 369px; width: 286px; text-align: center;
    font-size: 17px; font-weight: 700; color: var(--navy);
  }
  .calendar {
    position: absolute; left: 650px; top: 399px; width: 287px;
    border-collapse: collapse; table-layout: fixed;
  }
  .calendar th {
    height: 27px; background: var(--navy); color: var(--white);
    font-size: 13px; font-weight: 700;
    border: 2px solid var(--navy);
  }
  .calendar td {
    height: 33px; text-align: center;
    font-size: 13px; font-weight: 700; color: var(--navy);
    border: 2px solid var(--navy); background: var(--white);
  }
  .calendar .today span {
    display: inline-block; width: 34px; height: 27px; line-height: 27px;
    background: var(--navy); color: var(--white);
    outline: 2px solid var(--white); outline-offset: -4px;
  }
  .calendar .pager td {
    height: 27px; background: var(--navy); color: var(--white);
    font-size: 14px; text-align: left; padding: 0 4px;
  }
  .calendar .pager .next { text-align: right; }
  .footer {
    position: absolute; left: 192px; top: 727px; width: 960px; height: 80px;
    background: var(--navy-deep);
    border-top: 1px dashed #9aa5b1;
    text-align: center; color: var(--white);
  }
  .footer-nav {
    margin-top: 24px; font-size: 10px; letter-spacing: 0.3px;
  }
  .footer-nav .sep { color: #5aa0e0; margin: 0 7px; font-weight: 700; }
  .copyright { margin-top: 8px; font-size: 10px; }
</style>
</head>
<body>
<div class="page">
  <div class="top-rule"></div>
  <header class="header">
    <ul class="main-nav">
      <li>Home</li>
      <li>About Us</li>
      <li>About Mediation</li>
      <li>Scheduling</li>
      <li>Contact Us</li>
    </ul>
    <div class="brand"><span class="brand-mark"></span><span>Linden Mediation</span></div>
  </header>

  <main class="content">
    <div class="hero" role="img" aria-label="Group photo of the mediation team standing in a row in business suits"></div>

    <h2 class="section-title" style="left:16px; top:324px; width:600px;">About Us</h2>
    <p class="copy" style="left:16px; top:372px;">Lorem ipsum dolor sit amet, sectetu adip scing varius interdum incid unt quis, libero. Aenean mturpis. Maecenas hendrerit masa laoreet iaculipede mnisl ulamcorper. Tellus er sodales enim, in tincidunt mauris in odio. Massa ac laoreet iaculipede nisl ullamcorpermassa, ac consectetuer feipsum eget pede. Proin nunc. Donec massa. Nulla pulvinar, nisl ac convallis nonummy, tellus eros sodales enim, in tin- cidunt mauris in odio.</p>
    <div class="read-more" style="left:16px; top:447px;">read more</div>

    <h2 class="section-title" style="left:16px; top:479px; width:600px;">About Mediation</h2>
    <p class="copy" style="left:16px; top:528px;">Lorem ipsum dolor sit amet, sectetu adip scing varius interdum incid unt quis, libero. Aenean mturpis. Maecenas hendrerit masa laoreet iaculipede mnisl ulamcorper. Tellus er sodales enim, in tincidunt mauris in odio. Massa ac laoreet iaculipede nisl ullamcorpermassa, ac consectetuer feipsum eget pede. Proin nunc. Donec massa. Nulla pulvinar, nisl ac convallis nonummy, tellus eros sodales enim, in tin- cidunt mauris in odio.</p>
    <div class="read-more" style="left:16px; top:603px;">read more</div>

    <h2 class="section-title" style="left:648px; top:324px; width:290px;">Scheduling</h2>
    <div class="calendar-month">June 2011</div>
    <table class="calendar">
      <thead>
        <tr><th>M</th><th>T</th><th>W</th><th>T</th><th>F</th><th>S</th><th>S</th></tr>
      </thead>
      <tbody>
        <tr><td colspan="2"></td><td>1</td><td>2</td><td>3</td><td>4</td><td>5</td></tr>
        <tr><td class="today"><span>6</span></td><td>7</td><td>8</td><td>9</td><td>10</td><td>11</td><td>12</td></tr>
        <tr><td>13</td><td>14</td><td>15</td><td>16</td><td>17</td><td>18</td><td>19</td></tr>
        <tr><td>20</td><td>21</td><td>22</td><td>23</td><td>24</td><td>25</td><td>26</td></tr>
        <tr><td>27</td><td>28</td><td>29</td><td>30</td><td>31</td><td colspan="2"></td></tr>
        <tr class="pager"><td colspan="3">« May</td><td colspan="4" class="next">Jul »</td></tr>
      </tbody>
    </table>
  </main>

  <footer class="footer">
    <div class="footer-nav">HOME<span class="sep">|</span>ABOUT US<span class="sep">|</span>ABOUT MEDIATION<span class="sep">|</span>SCHEDULING<span class="sep">|</span>CONTACT US</div>
    <div class="copyright">Copyright © Linden Mediation.</div>
  </footer>
</div>
</body>
</html>
```